Our website, is loosely based on a grant proposal submitted to the Northern Vascular Society last year for a community-based project that could improve the health of the community at large, I have attached this file for your review (underline "loosely). The idea is to create a "patient navigator" a website where patients can both learn and use as a resource for their care. I have been working on the project for some time, but my other responsibilities as a cardiologist have not allowed me time to learn and design a website of this type. Our website is intended for a spanish speaking audience and is in Spanish language. Designs in english will have to be translated. Our name: AcademiaBrisa.com: means a health university: One option is to have the website have a "university" theme. The project calls for: An initial: easy registration process: collecting name, DOB and city. Simplicity is key, many of our patients barely use computers, and this site is meant to make things easier, not complicate them. The web site should work as an extension of the doctors office, so it should be serious, creative, addictive, engaging. Doctors will see the patients in the office then refer them to the website to continue their learning about their conditions. There should be a page where patients can post questions: a panel of doctors: represented with their pictures, (in circles? around the question answered?) titles and small resumes (our "faculty") answers them. Every person that will attach themself to this website will have a title: doctors and nurses will be professors, residents and fellows will be assistant professors, aids can be PA?. The site should have a market place where people can purchase items that doctors recommend including foods, products and devices; here too, we can have a "bookshop". This should have a flexible mechanism for doctors to add their recommendations a patients can have access to them. Very important: there should be a site intended to be a classroom, this is the meat of this protect: where people can watch videos our staff will make to learn about different subjects; the site should keep track of the videos watched by the person and eventually "graduate them". These videos will be created by my staff, and added over time to the site, students should be able to "request" classes (videos). It should have a site where people can input their medications (notebook), have them stored and printed as a list if necessary. And finally it should have a contact and references section. We have set up a relationship with another site that help people count calories: and a link to this should be available. We have a link to our twitter account, This protect is intended to expand, and we hope to establish a long term relationship with the design team to expand it as needed in the future. The site is on PageHarbor and can be seen in its current form at AcademiaBrisa.com . We have had a logo designed with specific colors of the hospital I work with and one plan is to present it to our hospital to adopt our page in it final form. Again, this site is in spanish and intended for a spanish audience.

Target Market(s)

Spanish speaking, late 30s to early 60s audience.

Industry/Entity Type

Community

Number of Pages Required

Font styles to use
Sans Serif

Colors
a64599
fceff5
3277b5

Requirements
Must have
• A simple, accesible look
Nice to have
• Animations, moving parts
Should not have
• English

```html
<!DOCTYPE html>
<html lang="es">
<head>
<meta charset="utf-8">
<title>AcademiaBrisa</title>
<link rel="stylesheet" href="https://fonts.googleapis.com/css2?family=Roboto:wght@300;400;500;700&display=swap">
<style>
  :root {
    --purple: #a64599;
    --pink: #fceff5;
    --blue: #3277b5;
    --navy: #24507e;
    --ink: #333;
    --muted: #666;
    --line: #ececec;
    --light-blue: #a9c7e4;
    --light-purple: #d7a3cf;
  }
  * { box-sizing: border-box; margin: 0; padding: 0; }
  html, body { width: 1084px; height: 1200px; overflow: hidden; }
  body { font-family: "Roboto", Arial, sans-serif; color: var(--ink); background: #fff; position: relative; }
  .site-header { height: 101px; background: var(--pink); position: relative; }
  .brand { position: absolute; left: 155px; top: 34px; font-size: 27px; font-weight: 300; color: var(--purple); letter-spacing: -0.5px; }
  .main-nav { position: absolute; left: 431px; top: 44px; display: flex; gap: 27px; font-size: 12px; font-weight: 400; color: #333; }
  .main-nav .active { color: var(--purple); }
  .header-social { position: absolute; left: 843px; top: 45px; display: flex; gap: 10px; }
  .header-social span { width: 13px; height: 13px; border-radius: 50%; background: #c7c7c7; }
  .infographic { position: absolute; top: 101px; left: 0; }
  .infographic text { font-family: "Roboto", Arial, sans-serif; }
  .cta-band { position: absolute; left: 0; width: 1084px; height: 88px; background: var(--blue); }
  .cta-band .cta-text { position: absolute; left: 157px; top: 31px; font-size: 20px; color: #fff; letter-spacing: 0.2px; }
  .cta-band .cta-button { position: absolute; left: 681px; top: 22px; width: 248px; height: 44px; background: var(--navy); color: #fff; font-size: 15px; display: flex; align-items: center; justify-content: center; letter-spacing: 0.3px; }
  .band-top { top: 487px; }
  .band-bottom { top: 1056px; }
  .band-bottom .cta-text { left: 156px; }
  .welcome { position: absolute; top: 575px; left: 0; width: 1084px; height: 222px; background: #fff; }
  .welcome h1 { position: absolute; left: 157px; top: 48px; font-size: 23px; font-weight: 300; color: #222; }
  .welcome h1 .brand-name { color: var(--purple); }
  .welcome p { position: absolute; left: 156px; top: 81px; width: 382px; font-size: 10px; line-height: 12px; color: var(--muted); }
  .read-more { position: absolute; left: 155px; top: 138px; width: 110px; height: 32px; background: var(--purple); color: #fff; font-size: 10px; font-weight: 500; display: flex; align-items: center; justify-content: center; }
  .video { position: absolute; left: 589px; top: 27px; width: 341px; height: 167px; border: 1px solid #ccc; background: linear-gradient(90deg, #e9dccd 0%, #d8d2c4 45%, #c9c4bb 100%); }
  .video svg { position: absolute; left: 146px; top: 60px; }
  .features { position: absolute; top: 797px; left: 0; width: 1084px; height: 259px; background: var(--pink); }
  .feature { position: absolute; width: 380px; height: 90px; }
  .feature .avatar { position: absolute; left: 0; top: 0; width: 88px; height: 88px; border-radius: 50%; border: 2px solid var(--purple); background: linear-gradient(135deg, #c9b7a5, #8a7a6e); }
  .feature h3 { position: absolute; left: 100px; top: 25px; font-size: 10px; font-weight: 500; color: var(--purple); }
  .feature p { position: absolute; left: 100px; top: 40px; width: 275px; font-size: 10px; line-height: 12px; color: var(--muted); }
  .f1 { left: 155px; top: 30px; } .f2 { left: 569px; top: 30px; }
  .f3 { left: 155px; top: 139px; } .f4 { left: 569px; top: 139px; }
  .f2 .avatar { background: linear-gradient(135deg, #7aa7c9, #3a5e7f); }
  .f3 .avatar { background: linear-gradient(135deg, #3e6b8a, #c89a8a); }
  .f4 .avatar { background: linear-gradient(135deg, #8fb6d6, #a38a78); }
  .site-footer { position: absolute; top: 1144px; left: 0; width: 1084px; height: 56px; background: #fff; }
  .site-footer .copyright { position: absolute; left: 155px; top: 22px; font-size: 12px; color: #888; display: flex; align-items: center; gap: 8px; }
  .site-footer .copyright i { width: 13px; height: 13px; border-radius: 50%; background: var(--purple); display: inline-block; }
  .footer-social { position: absolute; left: 808px; top: 16px; display: flex; gap: 8px; }
  .footer-social span { width: 24px; height: 24px; border-radius: 50%; background: #8e8e8e; }
</style>
</head>
<body>
<header class="site-header">
  <div class="brand">AcademiaBrisa</div>
  <nav class="main-nav">
    <span class="active">INICIO</span><span>ACERCA</span><span>TIENDA</span><span>BLOG</span><span>FAQ</span><span>CONTACTO</span>
  </nav>
  <div class="header-social" aria-label="Redes sociales"><span></span><span></span><span></span><span></span></div>
</header>

<svg class="infographic" width="1084" height="386" viewBox="0 0 1084 386" xmlns="http://www.w3.org/2000/svg">
  <defs>
    <symbol id="person" viewBox="0 0 20 40">
      <circle cx="10" cy="6" r="5" fill="none" stroke="currentColor" stroke-width="1.8"/>
      <path d="M3 38 V15 Q3 12 6 12 H14 Q17 12 17 15 V38 M7 38 V24 M13 38 V24" fill="none" stroke="currentColor" stroke-width="1.8"/>
    </symbol>
    <symbol id="pin" viewBox="0 0 10 14">
      <path d="M5 13 C2 9 1 7 1 5 A4 4 0 0 1 9 5 C9 7 8 9 5 13Z" fill="currentColor"/>
      <circle cx="5" cy="5" r="1.6" fill="#fff"/>
    </symbol>
  </defs>
  <rect width="1084" height="386" fill="#fff"/>
  <g stroke="var(--line)" stroke-width="1.5" fill="none">
    <path d="M104 0 V193 M395 0 V386 M620 0 V386 M0 96 H104 M0 193 H395 M733 0 V97 M620 97 H845 M845 0 V193 M963 0 V193 M845 117 H1084 M620 193 H1084 M900 193 V386 M900 256 H1084 M900 322 H1084"/>
  </g>

  <!-- clínicas / oficinas -->
  <circle cx="56" cy="47" r="39" fill="none" stroke="var(--blue)" stroke-width="2.5"/>
  <use href="#pin" x="25" y="40" width="9" height="12" color="var(--blue)"/>
  <text x="36" y="51" font-size="10" font-weight="500" fill="var(--blue)">CLÍNICAS</text>
  <circle cx="56" cy="144" r="39" fill="none" stroke="var(--purple)" stroke-width="2.5"/>
  <use href="#pin" x="24" y="137" width="9" height="12" color="var(--purple)"/>
  <text x="35" y="148" font-size="10" font-weight="500" fill="var(--purple)">OFICINAS</text>
  <rect x="116" y="20" width="272" height="140" fill="#d9d9d9" role="img" aria-label="Mapa mundial con clínicas y oficinas señaladas"/>

  <!-- cuadrícula de personas -->
  <g color="var(--blue)">
    <use href="#person" x="16" y="204" width="18" height="36"/><use href="#person" x="38" y="204" width="18" height="36"/><use href="#person" x="59" y="204" width="18" height="36"/><use href="#person" x="81" y="204" width="18" height="36"/><use href="#person" x="102" y="204" width="18" height="36"/><use href="#person" x="124" y="204" width="18" height="36"/><use href="#person" x="145" y="204" width="18" height="36"/><use href="#person" x="167" y="204" width="18" height="36"/>
    <use href="#person" x="16" y="292" width="18" height="36"/><use href="#person" x="38" y="292" width="18" height="36"/><use href="#person" x="59" y="292" width="18" height="36"/><use href="#person" x="81" y="292" width="18" height="36"/><use href="#person" x="102" y="292" width="18" height="36"/><use href="#person" x="124" y="292" width="18" height="36"/><use href="#person" x="145" y="292" width="18" height="36"/><use href="#person" x="167" y="292" width="18" height="36"/>
  </g>
  <g color="var(--purple)">
    <use href="#person" x="16" y="248" width="18" height="36"/><use href="#person" x="38" y="248" width="18" height="36"/><use href="#person" x="59" y="248" width="18" height="36"/><use href="#person" x="81" y="248" width="18" height="36"/><use href="#person" x="102" y="248" width="18" height="36"/><use href="#person" x="124" y="248" width="18" height="36"/><use href="#person" x="145" y="248" width="18" height="36"/><use href="#person" x="167" y="248" width="18" height="36"/>
    <use href="#person" x="16" y="336" width="18" height="36"/><use href="#person" x="38" y="336" width="18" height="36"/><use href="#person" x="59" y="336" width="18" height="36"/><use href="#person" x="81" y="336" width="18" height="36"/><use href="#person" x="102" y="336" width="18" height="36"/><use href="#person" x="124" y="336" width="18" height="36"/><use href="#person" x="145" y="336" width="18" height="36"/><use href="#person" x="167" y="336" width="18" height="36"/>
  </g>

  <!-- anillos (r=36, circunferencia 226) -->
  <g fill="none" stroke-width="9">
    <circle cx="243" cy="246" r="36" stroke="var(--light-blue)"/>
    <circle cx="243" cy="246" r="36" stroke="var(--blue)" stroke-dasharray="150 226" transform="rotate(-90 243 246)"/>
    <circle cx="339" cy="246" r="36" stroke="var(--light-purple)"/>
    <circle cx="339" cy="246" r="36" stroke="var(--purple)" stroke-dasharray="75 226" transform="rotate(-90 339 246)"/>
    <circle cx="243" cy="333" r="36" stroke="var(--light-purple)"/>
    <circle cx="243" cy="333" r="36" stroke="var(--purple)" stroke-dasharray="120 226" transform="rotate(-90 243 333)"/>
    <circle cx="339" cy="333" r="36" stroke="var(--light-blue)"/>
    <circle cx="339" cy="333" r="36" stroke="var(--blue)" stroke-dasharray="102 226" transform="rotate(-90 339 333)"/>
  </g>
  <g font-size="22" font-weight="500" text-anchor="middle">
    <text x="243" y="254" fill="var(--blue)">33%</text>
    <text x="339" y="254" fill="var(--purple)">75%</text>
    <text x="243" y="341" fill="var(--purple)">45%</text>
    <text x="339" y="341" fill="var(--blue)">55%</text>
  </g>

  <!-- columna central -->
  <path d="M508 76 V165 M508 252 V310" stroke="#f3dbe6" stroke-width="4"/>
  <circle cx="508" cy="44" r="31" fill="#fff" stroke="var(--blue)" stroke-width="2"/>
  <use href="#person" x="499" y="26" width="18" height="36" color="var(--blue)"/>
  <text x="488" y="111" font-size="24" font-weight="700" fill="var(--blue)" text-anchor="middle">6</text>
  <text x="520" y="106" font-size="9" font-weight="500" fill="var(--blue)">CARDIÓLOGOS</text>
  <circle cx="508" cy="192" r="58" fill="#fff" stroke="#fbe6ee" stroke-width="6"/>
  <text x="508" y="197" font-size="15" font-weight="300" fill="var(--purple)" text-anchor="middle">AcademiaBrisa</text>
  <text x="476" y="292" font-size="26" font-weight="700" fill="var(--purple)" text-anchor="middle">350</text>
  <text x="520" y="285" font-size="9" font-weight="500" fill="var(--purple)">PACIENTES</text>
  <circle cx="508" cy="342" r="31" fill="#fff" stroke="var(--purple)" stroke-width="2"/>
  <use href="#person" x="499" y="324" width="18" height="36" color="var(--purple)"/>

  <!-- celdas de cifras -->
  <use href="#person" x="630" y="14" width="36" height="72" color="var(--blue)"/>
  <text x="697" y="47" font-size="34" font-weight="700" fill="var(--blue)" text-anchor="middle">6</text>
  <text x="697" y="63" font-size="9" fill="var(--blue)" text-anchor="middle">cardiólogos</text>
  <text x="697" y="74" font-size="9" fill="var(--blue)" text-anchor="middle">multilingües</text>
  <use href="#person" x="741" y="14" width="36" height="72" color="var(--purple)"/>
  <text x="810" y="52" font-size="26" font-weight="700" fill="var(--purple)" text-anchor="middle">350</text>
  <text x="810" y="68" font-size="9" fill="var(--purple)" text-anchor="middle">Pacientes</text>
  <g fill="none" stroke="var(--blue)" stroke-width="2">
    <rect x="663" y="131" width="33" height="30" rx="2"/><path d="M663 141 H696"/>
  </g>
  <g fill="var(--blue)"><rect x="668" y="146" width="5" height="4"/><rect x="677" y="146" width="5" height="4"/><rect x="686" y="146" width="5" height="4"/><rect x="668" y="153" width="5" height="4"/><rect x="677" y="153" width="5" height="4"/><rect x="686" y="153" width="5" height="4"/></g>
  <text x="720" y="156" font-size="32" font-weight="700" fill="var(--blue)" text-anchor="middle">1</text>
  <text x="737" y="146" font-size="9" font-weight="500" fill="var(--blue)">VISITA SEMANAL</text>
  <g color="var(--blue)">
    <use href="#person" x="897" y="22" width="18" height="36"/>
    <use href="#person" x="878" y="76" width="15" height="30"/><use href="#person" x="898" y="76" width="15" height="30"/><use href="#person" x="918" y="76" width="15" height="30"/>
  </g>
  <g color="var(--purple)">
    <use href="#person" x="1013" y="22" width="18" height="36"/>
    <use href="#person" x="994" y="76" width="15" height="30"/><use href="#person" x="1014" y="76" width="15" height="30"/><use href="#person" x="1034" y="76" width="15" height="30"/>
  </g>
  <text x="907" y="156" font-size="27" font-weight="700" fill="var(--navy)" text-anchor="middle">100</text>
  <text x="907" y="171" font-size="9" fill="var(--navy)" text-anchor="middle">INDIVIDUOS</text>
  <text x="1022" y="156" font-size="27" font-weight="700" fill="var(--purple)" text-anchor="middle">100</text>
  <text x="1022" y="171" font-size="9" fill="var(--purple)" text-anchor="middle">PERSONAS</text>

  <!-- gráfico de líneas -->
  <g stroke="#e4e4e4" stroke-width="1" fill="none">
    <rect x="632" y="217" width="248" height="106"/>
    <path d="M674 217 V323 M715 217 V323 M757 217 V323 M798 217 V323 M839 217 V323 M632 252 H880 M632 288 H880"/>
  </g>
  <polyline points="632,323 731,265 771,288 811,252 831,261 876,221" fill="none" stroke="var(--blue)" stroke-width="2"/>
  <polyline points="632,295 668,278 716,294 771,254 842,286 876,242" fill="none" stroke="var(--purple)" stroke-width="2"/>
  <g fill="#fff" stroke="var(--blue)" stroke-width="2"><circle cx="731" cy="265" r="5"/><circle cx="771" cy="288" r="5"/><circle cx="811" cy="252" r="5"/><circle cx="831" cy="261" r="5"/><circle cx="876" cy="221" r="5"/></g>
  <g fill="#fff" stroke="var(--purple)" stroke-width="2"><circle cx="668" cy="278" r="5"/><circle cx="716" cy="294" r="5"/><circle cx="771" cy="254" r="5"/><circle cx="842" cy="286" r="5"/><circle cx="876" cy="242" r="5"/></g>
  <path d="M647 363 L634 351 A7 7 0 0 1 647 343 A7 7 0 0 1 660 351Z" fill="var(--purple)"/>
  <text x="667" y="356" font-size="9" font-weight="500" fill="var(--purple)">Atención médica</text>
  <path d="M758 346 L776 339 L794 346 L776 353Z M766 350 V357 Q776 362 786 357 V350" fill="none" stroke="var(--blue)" stroke-width="2"/>
  <text x="803" y="356" font-size="9" font-weight="500" fill="var(--blue)">Educación en salud</text>

  <!-- lista derecha -->
  <rect x="935" y="216" width="24" height="15" rx="3" fill="var(--blue)"/>
  <g fill="#fff"><circle cx="942" cy="223.5" r="1.5"/><circle cx="947" cy="223.5" r="1.5"/><circle cx="952" cy="223.5" r="1.5"/></g>
  <circle cx="922" cy="222" r="7" fill="var(--blue)"/>
  <text x="972" y="226" font-size="9" font-weight="500" fill="var(--blue)">Entender inglés</text>
  <path d="M916 280 Q924 276 930 282 Q936 276 944 280 V296 Q936 292 930 298 Q924 292 916 296Z M930 282 V298" fill="none" stroke="var(--purple)" stroke-width="2"/>
  <text x="972" y="292" font-size="9" font-weight="500" fill="var(--purple)">Sesgos culturales</text>
  <g fill="var(--blue)"><rect x="915" y="360" width="4" height="10"/><rect x="921" y="356" width="4" height="14"/><rect x="927" y="352" width="4" height="18"/><rect x="933" y="348" width="4" height="22"/></g>
  <path d="M914 356 L936 338 M929 338 H937 V346" fill="none" stroke="var(--blue)" stroke-width="2"/>
  <text x="972" y="359" font-size="9" font-weight="500" fill="var(--navy)">Nivel socioeconómico</text>
</svg>

<section class="cta-band band-top">
  <div class="cta-text">¡CONTÁCTENOS Y MEJORE SU SALUD!</div>
  <div class="cta-button">PEDIR UNA CITA</div>
</section>

<section class="welcome">
  <h1>Bienvenidos a <span class="brand-name">AcademiaBrisa</span></h1>
  <p>Lorem ipsum dolor sit amet, consectetuer adipiscing elit, sed diam nonummy nibhdf euismod tincidunt ut laoreet dolore magna aliquam erat volutpat. Ut wisi enim adsdv minim veniam, quis nostrud exerci tation ullamcorper suscipit lobortis nisl ut aliquips ex ea commodo consequat.  autem vel eum iriure dolor in hendrerit in vulputate velit</p>
  <div class="read-more">LEER MÁS</div>
  <div class="video" role="img" aria-label="Video: una doctora joven conversa con una paciente mayor en un sofá">
    <svg width="48" height="48" viewBox="0 0 48 48" aria-hidden="true">
      <circle cx="24" cy="24" r="21" fill="rgba(255,255,255,0.55)" stroke="#333" stroke-width="4"/>
      <path d="M19 14 L34 24 L19 34Z" fill="#333"/>
    </svg>
  </div>
</section>

<section class="features">
  <div class="feature f1"><div class="avatar" role="img" aria-label="Foto: mujer joven usando una tableta"></div><h3>LOREM IPSUM DOLOR SIT AMET, ?</h3><p>Lorem ipsum dolor sit amet, consectetuer adipiscing elit, diam nonummy nibhdf euismod tincidunt ut laoreet dolore.</p></div>
  <div class="feature f2"><div class="avatar" role="img" aria-label="Foto: hombre sonriente con una tableta"></div><h3>LOREM IPSUM DOLOR SIT AMET, ?</h3><p>Lorem ipsum dolor sit amet, consectetuer adipiscing elit, diam nonummy nibhdf euismod tincidunt ut laoreet dolore.</p></div>
  <div class="feature f3"><div class="avatar" role="img" aria-label="Foto: mujer leyendo en una biblioteca"></div><h3>LOREM IPSUM DOLOR SIT AMET, ?</h3><p>Lorem ipsum dolor sit amet, consectetuer adipiscing elit, diam nonummy nibhdf euismod tincidunt ut laoreet dolore.</p></div>
  <div class="feature f4"><div class="avatar" role="img" aria-label="Foto: hombre consultando una tableta"></div><h3>LOREM IPSUM DOLOR SIT AMET, ?</h3><p>Lorem ipsum dolor sit amet, consectetuer adipiscing elit, diam nonummy nibhdf euismod tincidunt ut laoreet dolore.</p></div>
</section>

<section class="cta-band band-bottom">
  <div class="cta-text">PARA APRENDER, ¡SOLICITE CLASES EN VIDEO!</div>
  <div class="cta-button">SOLICITAR CLASES</div>
</section>

<footer class="site-footer">
  <div class="copyright"><i></i>Derechos reservados © 2014 AcademiaBrisa</div>
  <div class="footer-social" aria-label="Redes sociales"><span></span><span></span><span></span><span></span></div>
</footer>
</body>
</html>
```